Billboard design - consider what a billboard is

Design a billboard using my logo - Billboard is 6m x 3m
A Billboard is advertising for my company that is on a big sign.

Has to be clean and easy to read, and ideally highlights that we are Residential and Commercial builders.

Keep it clean and easy to read

The contact number for the board is

022 583 7092
www.harbourframeworks.co.nz
info@harbourframeworks.co.nz

Doesnt have to have all contact details if it doesnt fit

Has to catch peoples attention to contact us if they need a builder

Can you please change the sign to be all white writing, with black background ?
Updates

Please consider what a billboard is...

The design needs to be suitable for a billboard..

Target Market(s)

people driving past

Industry/Entity Type

Construction

Logo Text

Wellington Builder, website email address, contact number

Colors
0054AA
0677BA
7BADD7
CADEEF
E8F1F8

Requirements
Must have
• Easy to read
Nice to have
• easy to read, can clearly see contact details

```html
<!DOCTYPE html>
<html lang="en">
<head>
<meta charset="utf-8">
<title>Harbour Frameworks Billboard</title>
<link rel="stylesheet" href="https://fonts.googleapis.com/css2?family=Roboto+Condensed:wght@700&family=Arimo:wght@700&display=swap">
<style>
  :root {
    --brand-blue: #588ccb;
    --text: #ffffff;
    --background: #000000;
    --slate: #8a8584;
  }
  * { margin: 0; padding: 0; box-sizing: border-box; }
  html, body { width: 1200px; height: 600px; overflow: hidden; background: var(--background); }
  .billboard {
    position: relative;
    width: 1200px;
    height: 600px;
    background: var(--background);
    overflow: hidden;
    font-family: "Roboto Condensed", "Arial Narrow", sans-serif;
    color: var(--text);
  }
  .brand {
    position: absolute;
    left: 44px;
    top: 62px;
    color: var(--brand-blue);
    font-weight: 700;
    line-height: 1;
  }
  .brand-name { display: block; font-size: 66px; letter-spacing: -0.5px; }
  .brand-sub { display: block; font-size: 22px; letter-spacing: 1.5px; margin-top: 4px; }
  .headline {
    position: absolute;
    left: 32px;
    top: 206px;
    font-size: 60px;
    font-weight: 700;
    line-height: 61.5px;
    letter-spacing: 0;
    text-transform: uppercase;
    white-space: nowrap;
    transform: scaleX(0.88);
    transform-origin: left top;
  }
  .phone-band {
    position: absolute;
    left: 0;
    top: 410px;
    width: 771px;
    height: 126px;
    background: var(--brand-blue);
  }
  .phone-number {
    position: absolute;
    left: 31px;
    top: 10px;
    font-family: "Arimo", Arial, sans-serif;
    font-weight: 700;
    font-size: 105px;
    line-height: 105px;
    color: var(--text);
    letter-spacing: 2px;
    white-space: nowrap;
  }
  .contact-line {
    position: absolute;
    left: 32px;
    top: 549px;
    font-size: 29px;
    font-weight: 700;
    line-height: 34px;
    white-space: nowrap;
    color: var(--text);
  }
  .project-panel {
    position: absolute;
    left: 799px;
    top: 0;
    width: 401px;
    height: 600px;
  }
</style>
</head>
<body>
<main class="billboard">
  <div class="brand">
    <span class="brand-name">Harbour</span>
    <span class="brand-sub">FRAMEWORKS</span>
  </div>

  <h1 class="headline">Residential renovations,<br>new builds, and commercial<br>construction.</h1>

  <div class="phone-band">
    <p class="phone-number">022 583 7092</p>
  </div>

  <p class="contact-line">harbourframeworks.co.nz | info@harbourframeworks.co.nz</p>

  <svg class="project-panel" viewBox="1715 0 861 1288" preserveAspectRatio="none" xmlns="http://www.w3.org/2000/svg">
    <defs>
      <linearGradient id="houses-tone" x1="0" y1="0" x2="0" y2="1">
        <stop offset="0" stop-color="#4f8fd6"/>
        <stop offset="0.3" stop-color="#8cb7e6"/>
        <stop offset="0.5" stop-color="#c9c4bc"/>
        <stop offset="0.75" stop-color="#b08f68"/>
        <stop offset="1" stop-color="#6b6b6b"/>
      </linearGradient>
      <linearGradient id="office-tone" x1="0" y1="0" x2="0" y2="1">
        <stop offset="0" stop-color="#9a9792"/>
        <stop offset="0.5" stop-color="#8a6a3c"/>
        <stop offset="1" stop-color="#5a4636"/>
      </linearGradient>
      <linearGradient id="heritage-tone" x1="0" y1="0" x2="0" y2="1">
        <stop offset="0" stop-color="#4f8fd6"/>
        <stop offset="0.35" stop-color="#a9b9c9"/>
        <stop offset="0.6" stop-color="#cfcbc0"/>
        <stop offset="1" stop-color="#5b5f63"/>
      </linearGradient>
    </defs>
    <rect x="1715" y="0" width="861" height="1288" fill="#000000"/>
    <polygon role="img" aria-label="Photo of new two-storey townhouses with timber fencing" points="1715,0 2107,0 2107,520 1715,905" fill="url(#houses-tone)"/>
    <polygon role="img" aria-label="Photo of a commercial building under construction with scaffolding" points="2107,645 2107,1288 1715,1288 1715,1035" fill="url(#office-tone)"/>
    <polygon points="2183,0 2455,0 2183,270" fill="#588ccb"/>
    <polygon role="img" aria-label="Photo of a renovated heritage commercial building" points="2530,0 2576,0 2576,1130 2420,1288 2183,1288 2183,345" fill="url(#heritage-tone)"/>
    <polygon points="2576,1150 2576,1288 2440,1288" fill="#8a8584"/>
  </svg>
</main>
</body>
</html>
```